Letterhead, stationery and email signature for construction business

I need the letterhead, stationery and email signature designs for a construction business. I want them to have a corporate feel to them.

I've attached the logo for reference.

```html
<!DOCTYPE html>
<html lang="en">
<head>
<meta charset="utf-8">
<title>Halvern Projects – Business Card</title>
<link href="https://fonts.googleapis.com/css2?family=Montserrat:wght@400;500;700&display=swap" rel="stylesheet">
<style>
  :root {
    --brand-blue: #2f58b0;
    --brand-blue-deep: #25479a;
    --ink-grey: #5f6066;
    --rule-grey: #6b6c70;
    --card-white: #ffffff;
    --backdrop: #d9d9d7;
  }
  * { box-sizing: border-box; margin: 0; padding: 0; }
  html, body {
    width: 1200px;
    height: 801px;
    overflow: hidden;
  }
  body {
    background: var(--backdrop);
    font-family: "Montserrat", sans-serif;
    display: flex;
    align-items: center;
    justify-content: center;
    gap: 48px;
  }
  .card {
    width: 530px;
    height: 303px;
    border-radius: 3px;
    box-shadow: 0 6px 18px rgba(0,0,0,0.18);
    position: relative;
    overflow: hidden;
  }
  .card-front {
    background: var(--card-white);
    display: flex;
    align-items: center;
  }
  .brand-block {
    width: 250px;
    display: flex;
    align-items: center;
    justify-content: center;
    gap: 10px;
  }
  .brand-square {
    width: 22px;
    height: 22px;
    background: var(--brand-blue);
  }
  .brand-name {
    font-weight: 700;
    font-size: 21px;
    color: var(--brand-blue);
    letter-spacing: 0.5px;
    text-transform: uppercase;
  }
  .divider {
    width: 1px;
    height: 200px;
    background: var(--rule-grey);
  }
  .contact-block {
    padding-left: 26px;
    color: var(--ink-grey);
  }
  .person-name {
    font-weight: 700;
    font-size: 19px;
    color: var(--brand-blue);
    text-transform: uppercase;
    letter-spacing: 0.3px;
  }
  .person-role {
    font-weight: 700;
    font-size: 14px;
    color: var(--ink-grey);
    margin-bottom: 14px;
  }
  .address {
    font-size: 11.5px;
    line-height: 1.45;
    margin-bottom: 8px;
  }
  .contact-list { list-style: none; }
  .contact-list li {
    display: flex;
    align-items: center;
    gap: 7px;
    font-size: 11.5px;
    line-height: 1.6;
  }
  .contact-list svg {
    width: 11px;
    height: 11px;
    flex: none;
  }
  .card-back {
    background: linear-gradient(135deg, var(--brand-blue) 0%, var(--brand-blue-deep) 100%);
  }
</style>
</head>
<body>
  <section class="card card-front">
    <div class="brand-block">
      <span class="brand-square"></span>
      <span class="brand-name">Halvern Projects</span>
    </div>
    <div class="divider"></div>
    <div class="contact-block">
      <h1 class="person-name">Marcus Doyle</h1>
      <p class="person-role">President</p>
      <p class="address">Halvern Projects Ltd.<br>Ashby House, 14 Kingsley<br>Rd, London SE4 7QT</p>
      <ul class="contact-list">
        <li>
          <svg viewBox="0 0 12 12" aria-hidden="true"><path d="M2.5 1 L4.5 1 L5.2 3.6 L3.9 4.6 C4.6 6 5.9 7.3 7.4 8 L8.4 6.8 L11 7.5 L11 9.5 C11 10.3 10.3 11 9.5 11 C5 11 1 7 1 2.5 C1 1.7 1.7 1 2.5 1 Z" fill="#2f58b0"/></svg>
          (555) 318-4400
        </li>
        <li>
          <svg viewBox="0 0 12 12" aria-hidden="true"><rect x="0.8" y="2.3" width="10.4" height="7.4" fill="none" stroke="#2f58b0" stroke-width="1.2"/><path d="M1 2.6 L6 6.6 L11 2.6" fill="none" stroke="#2f58b0" stroke-width="1.2"/></svg>
          info@halvernprojects.com
        </li>
        <li>
          <svg viewBox="0 0 12 12" aria-hidden="true"><circle cx="6" cy="6" r="5" fill="none" stroke="#2f58b0" stroke-width="1.1"/><ellipse cx="6" cy="6" rx="2.2" ry="5" fill="none" stroke="#2f58b0" stroke-width="1"/><path d="M1 6 H11 M2 3.5 H10 M2 8.5 H10" stroke="#2f58b0" stroke-width="0.9"/></svg>
          www.halvernprojects.com
        </li>
      </ul>
    </div>
  </section>

  <section class="card card-back" role="img" aria-label="Card reverse: repeating embossed pattern of the company emblem on brand blue"></section>
</body>
</html>
```